Logo & Responsive Website Design for Mortgage Company

Talvo Mortgage is a new Mortgage Fin-Tech company that will use its own innovative, proprietary technology for lead generation, mortgage origination, and processing of residential home loans in the US. The design should convey that we are a technology-driven company, offering borrowers seeking home loans an exceptional experience throughout the borrowing process.

We are looking for designs that are elegant, convey technical competency, simple to navigate, and set us apart from the competition.

We are not set on any particular colors at this point, so feel free to choose the best colors for your particular designs.

Please include both desktop and mobile designs.

Some Examples of Mortgage Websites. These are to show the typical content, not designs that we particularly like or dislike.
https://www.pondrel.example/
https://www.kmtfunding.example/
https://dulvamortgage.example/
https://wexo.example/
https://primecoastlending.example/

Please send comments with additional questions.

Thank You For your participation.

Target Market(s)

U.S. Residential Home Loan Seekers

Industry/Entity Type

FinTech Mortgage

Number of Pages Required

2 page

```html
<!DOCTYPE html>
<html lang="en">
<head>
<meta charset="utf-8">
<title>Talvo Mortgage</title>
<link href="https://fonts.googleapis.com/css2?family=Montserrat:wght@500;600;700;800&family=Roboto:wght@400;500;700&display=swap" rel="stylesheet">
<style>
:root{
  --orange:#f7931e;
  --orange-deep:#ef8a15;
  --dark:#1f1f24;
  --grey-btn:#5b5b60;
  --text:#3a3a3a;
  --muted:#6a6a6a;
  --cream:#fdf4ea;
  --white:#ffffff;
  --line:#e6e6e6;
}
*{box-sizing:border-box;margin:0;padding:0}
html,body{width:1200px;height:4285px;overflow:hidden}
body{position:relative;background:var(--white);font-family:'Roboto',sans-serif;color:var(--text)}
.abs{position:absolute}
.section-title{position:absolute;left:0;width:1200px;text-align:center;font-family:'Montserrat',sans-serif;font-weight:700;font-size:35px;color:var(--dark)}
.section-title::after{content:"";display:block;width:54px;height:4px;border-radius:2px;background:var(--orange);margin:10px auto 0}
.btn{position:absolute;display:flex;align-items:center;border-radius:30px;overflow:hidden;background:var(--orange);color:#fff;font-size:15px;font-weight:500;text-transform:uppercase;height:46px}
.btn .label{padding-left:22px;flex:1;white-space:nowrap}
.btn .arrow{width:58px;height:100%;background:var(--grey-btn);display:flex;align-items:center;justify-content:center;clip-path:polygon(22% 0,100% 0,100% 100%,0 100%)}
.btn .arrow svg{width:30px;height:12px}

/* header */
.site-header{position:absolute;top:0;left:0;width:1200px;height:120px;background:#fff;box-shadow:0 2px 6px rgba(0,0,0,.08);z-index:3}
.brand{position:absolute;left:100px;top:40px;display:flex;align-items:center;gap:10px;font-family:'Montserrat',sans-serif;font-weight:600;font-size:26px;color:var(--dark)}
.brand .mark{width:26px;height:26px;background:var(--orange);border-radius:4px}
.contact-chip{position:absolute;top:16px;display:flex;gap:14px;align-items:center}
.contact-chip .ic{width:38px;height:38px;border-radius:50%;background:#fff;box-shadow:0 2px 8px rgba(0,0,0,.12);display:flex;align-items:center;justify-content:center}
.contact-chip small{display:block;color:var(--orange);font-size:13px}
.contact-chip span{display:block;font-size:15px;color:var(--dark);margin-top:3px;white-space:nowrap}
.main-nav{position:absolute;top:84px;left:430px;display:flex;font-size:15px;color:var(--dark)}
.main-nav a{text-decoration:none;color:inherit;padding:0 30px;border-left:1px solid #333;line-height:14px}
.main-nav a:first-child{border-left:none;padding-left:0;color:var(--orange);text-decoration:underline;text-underline-offset:6px}
.main-nav a:last-child{padding-right:0}

/* hero */
.hero-photo{position:absolute;top:120px;left:0;width:1200px;height:700px;background:linear-gradient(90deg,#6f6f6f 0%,#9c9c9c 40%,#c7c7c7 70%,#b2b2b2 100%)}
.hero-copy{position:absolute;left:108px;top:306px;color:#fff}
.hero-copy .eyebrow{font-family:'Montserrat',sans-serif;font-weight:700;font-size:33px}
.hero-copy h1{font-family:'Montserrat',sans-serif;font-weight:800;font-size:54px;margin-top:6px}
.hero-copy p{font-size:15px;line-height:26px;margin-top:12px;width:430px}
.slider-dots{position:absolute;left:1124px;top:385px;display:flex;flex-direction:column;gap:12px}
.slider-dots i{width:12px;height:12px;border:1.5px solid #fff;border-radius:50%}
.slider-dots i.on{border-color:var(--orange);background:radial-gradient(var(--orange) 35%,transparent 40%)}

/* calculator */
.calculator{position:absolute;top:815px;left:0;width:1200px;height:390px;background:var(--cream)}
.calc-tabs{position:absolute;left:110px;top:20px;display:flex;gap:32px;font-size:21px;font-weight:500;color:var(--dark)}
.calc-tabs .active{color:var(--orange);border-bottom:3px solid var(--orange);padding-bottom:6px}
.field{position:absolute;top:80px;width:232px}
.field label{font-size:13px;color:var(--muted)}
.field .input{margin-top:12px;height:47px;border-radius:24px;background:#fff;box-shadow:0 2px 6px rgba(0,0,0,.06);padding-left:20px;display:flex;align-items:center;font-size:14px;color:#777}
.advanced{position:absolute;left:111px;top:183px;font-size:14px;color:var(--orange);text-decoration:underline}
.pay-label{position:absolute;left:110px;top:222px;font-size:15px;font-weight:500;color:var(--dark)}
.pay-total{position:absolute;left:777px;top:223px;font-size:15px;color:var(--orange)}
.pay-bar{position:absolute;left:110px;top:258px;width:695px;height:7px;border-radius:4px;background:#fff}
.pay-item{position:absolute;top:287px;display:flex;gap:20px;font-size:15px;color:var(--dark);line-height:22px}
.pay-item .dot{width:20px;height:20px;border-radius:50%;background:var(--orange);margin-top:12px}

/* about */
.about-frame{position:absolute;left:130px;top:1303px;width:220px;height:394px;border:2px solid var(--orange)}
.about-photo{position:absolute;left:148px;top:1322px;width:424px;height:362px;background:#fff;padding:10px;box-shadow:0 4px 16px rgba(0,0,0,.12)}
.about-photo div{width:100%;height:100%;background:linear-gradient(135deg,#6a6762,#a9a39a 50%,#d8d2c8)}
.about-copy{position:absolute;left:627px;top:1298px;width:459px}
.about-copy h2{font-family:'Montserrat',sans-serif;font-weight:700;font-size:35px;color:var(--dark)}
.about-copy h2::after{content:"";display:block;width:54px;height:4px;background:var(--orange);border-radius:2px;margin-top:8px}
.about-copy p{margin-top:20px;font-size:15px;line-height:25.8px;color:#555;text-align:justify}

/* services */
.services{position:absolute;top:1785px;left:0;width:1200px;height:592px;background:linear-gradient(180deg,var(--orange-deep),#f9a53a)}
.services .section-title{top:68px;color:#fff}
.services .section-title::after{background:#fff}
.service-card{position:absolute;top:147px;width:312px;height:370px;background:#fff;border-radius:14px;padding:8px}
.service-card .photo{height:185px;border-radius:8px}
.service-card h3{font-family:'Montserrat',sans-serif;font-weight:700;font-size:15px;color:var(--dark);margin:22px 16px 0}
.service-card p{font-size:14.5px;line-height:25px;color:#555;margin:12px 16px 0}
.service-card a{display:flex;align-items:center;gap:10px;font-size:14px;color:var(--orange);margin:6px 16px 0;text-decoration:underline}

/* why choose */
.why-card{position:absolute;top:2538px;width:236px;height:214px;background:#fff;border:1px solid var(--line);box-shadow:0 3px 10px rgba(0,0,0,.06);text-align:center}
.why-card svg.icon{margin-top:18px;width:72px;height:68px}
.why-card h3{font-family:'Roboto',sans-serif;font-weight:500;font-size:15px;color:var(--dark);margin-top:10px}
.why-card p{font-size:14px;line-height:23px;color:#555;margin:6px 14px 0}
.why-card .go{width:26px;height:26px;border:1.5px solid #333;border-radius:50%;margin:10px auto 0;display:flex;align-items:center;justify-content:center}
.why-card.active{background:var(--orange);border-color:var(--orange)}
.why-card.active h3,.why-card.active p{color:#fff}
.why-card.active .go{border-color:#fff}

/* testimonials */
.stars{position:absolute;left:0;width:1200px;top:2928px;text-align:center;color:var(--orange);font-size:20px;letter-spacing:4px}
.quote{position:absolute;left:178px;top:2962px;width:844px;text-align:center;font-size:15px;line-height:26px;color:#444}
.avatar{position:absolute;border-radius:50%}
.reviewer{position:absolute;left:0;width:1200px;top:3185px;text-align:center;font-size:17px;font-weight:500;color:var(--dark)}

/* contact */
.contact{position:absolute;top:3287px;left:0;width:1200px;height:560px;background:var(--cream)}
.contact .section-title{top:60px}
.form-field{position:absolute;width:318px;height:51px;border-radius:26px;background:#fff;box-shadow:0 2px 8px rgba(0,0,0,.05);padding-left:22px;display:flex;align-items:center;font-size:15px;color:#333}
.message{position:absolute;left:110px;top:275px;width:980px;height:143px;border-radius:22px;background:#fff;box-shadow:0 2px 8px rgba(0,0,0,.05);padding:22px;font-size:15px;color:#333}

/* footer */
.site-footer{position:absolute;top:3785px;left:0;width:1200px;height:500px;background:var(--dark);color:#fff}
.foot-col{position:absolute;top:180px}
.foot-col h4{font-size:16px;font-weight:500}
.foot-col ul{list-style:none;margin-top:20px}
.foot-col li{font-size:15px;line-height:34px;color:#eee}
.foot-col p{font-size:15px;line-height:23px;margin-top:20px;color:#eee}
.subscribe{margin-top:20px;width:225px;height:42px;border-radius:22px;background:#3a3a40;display:flex;align-items:center;justify-content:space-between;padding-left:16px;font-size:13px;color:#ccc;overflow:hidden}
.subscribe b{width:44px;height:42px;background:var(--orange);border-radius:0 22px 22px 0;display:flex;align-items:center;justify-content:center}
.contact-row{display:flex;gap:16px;margin-top:18px}
.contact-row small{display:block;font-size:12px;font-weight:700}
.contact-row span{display:block;font-size:15px;line-height:23px;color:#eee;margin-top:4px}
.foot-rule{position:absolute;left:110px;top:430px;width:980px;height:1px;background:#44444a}
.copyright{position:absolute;left:0;width:1200px;top:462px;text-align:center;font-size:15px;color:#eee}
.to-top{position:absolute;left:1118px;top:348px;width:36px;height:36px;border-radius:50%;background:var(--orange);display:flex;align-items:center;justify-content:center}
</style>
</head>
<body>

<header class="site-header">
  <div class="brand"><span class="mark"></span>Talvo Mortgage</div>
  <div class="contact-chip" style="left:446px">
    <span class="ic"><svg width="16" height="16" viewBox="0 0 24 24"><path d="M6.6 10.8a15 15 0 006.6 6.6l2.2-2.2a1 1 0 011-.25 11.4 11.4 0 003.6.57 1 1 0 011 1V20a1 1 0 01-1 1A17 17 0 013 4a1 1 0 011-1h3.5a1 1 0 011 1 11.4 11.4 0 00.57 3.6 1 1 0 01-.25 1z" fill="#f7931e"/></svg></span>
    <div><small>Call Us:</small><span>+1 555 014 2290</span></div>
  </div>
  <div class="contact-chip" style="left:658px">
    <span class="ic"><svg width="16" height="14" viewBox="0 0 24 18"><rect x="1" y="1" width="22" height="16" rx="2" fill="none" stroke="#f7931e" stroke-width="2"/><path d="M1 2l11 8 11-8" fill="none" stroke="#f7931e" stroke-width="2"/></svg></span>
    <div><small>Email Us:</small><span>info@talvo.example</span></div>
  </div>
  <div class="btn" style="left:910px;top:16px;width:176px;height:45px"><span class="label">Apply Now</span><span class="arrow"><svg viewBox="0 0 30 12"><path d="M0 6h27M22 1l6 5-6 5" stroke="#fff" stroke-width="2" fill="none"/></svg></span></div>
  <nav class="main-nav">
    <a>HOME</a><a>ABOUT US</a><a>SERVICES</a><a>WHY CHOOSE US</a><a>CONTACT US</a>
  </nav>
</header>

<div class="hero-photo" role="img" aria-label="Hand holding a small model house with a pen in the background"></div>
<div class="hero-copy">
  <div class="eyebrow">Welcome To</div>
  <h1>Talvo Mortgage</h1>
  <p>Lorem ipsum dolor sit amet consectetur adipiscing elit sed eiusmod tempor incididunt labore dolore magna aliquad.</p>
</div>
<div class="btn" style="left:108px;top:515px;width:176px;height:46px"><span class="label">Get Started</span><span class="arrow"><svg viewBox="0 0 30 12"><path d="M0 6h27M22 1l6 5-6 5" stroke="#fff" stroke-width="2" fill="none"/></svg></span></div>
<div class="slider-dots"><i></i><i></i><i class="on"></i><i></i><i></i></div>
<svg class="abs" style="left:0;top:715px" width="1200" height="110" viewBox="0 0 1200 110">
  <path d="M0 100L370 8L1200 70L1200 110L0 110Z" fill="#f7931e"/>
  <path d="M0 108L370 24L1200 86L1200 110L0 110Z" fill="#fdf4ea"/>
</svg>

<section class="calculator">
  <div class="calc-tabs"><span class="active">Mortgage Calculator</span><span>Refinance Calculator</span></div>
  <div class="field" style="left:110px"><label>Purchase Price</label><div class="input">$</div></div>
  <div class="field" style="left:359px"><label>Down Payment</label><div class="input">%</div></div>
  <div class="field" style="left:608px"><label>Loan Program</label><div class="input" style="justify-content:space-between;padding-right:18px">30- year Fixed<svg width="10" height="6" viewBox="0 0 10 6"><path d="M0 0h10L5 6z" fill="#333"/></svg></div></div>
  <div class="field" style="left:857px"><label>Rate</label><div class="input">%</div></div>
  <div class="advanced">Show Advanced Options</div>
  <div class="pay-label">Your Payment</div>
  <div class="pay-total">$0</div>
  <div class="pay-bar"></div>
  <div class="pay-item" style="left:113px"><span class="dot"></span><div>$0<br>Principal + Interest</div></div>
  <div class="pay-item" style="left:383px"><span class="dot"></span><div>$0<br>Taxes</div></div>
  <div class="pay-item" style="left:595px"><span class="dot"></span><div>$0<br>Insurance</div></div>
  <div class="btn" style="left:840px;top:238px;width:228px;height:47px"><span class="label">Start Application</span><span class="arrow"><svg viewBox="0 0 30 12"><path d="M0 6h27M22 1l6 5-6 5" stroke="#fff" stroke-width="2" fill="none"/></svg></span></div>
</section>

<div class="about-frame"></div>
<div class="about-photo"><div role="img" aria-label="Mortgage advisor meeting a couple at a table with documents"></div></div>
<div class="about-copy">
  <h2>About Us</h2>
  <p>Lorem ipsum dolor sit amet, consectetur adipiscing elit, sed do eiusmod tempor incididunt ut labore et dolore magna aliqua. Ut enim ad minim veniam, quis nostrud exercitation ullamco laboris nisi ut aliquip ex ea commodo consequat. Duis aute irure dolor in reprehenderit in voluptate velit esse cillum dolore eu fugiat nulla pariatur. Excepteur sint occaecat cupidatat non proident, sunt in culpa qui officia deserunt mollit anim id est laborum.Lorem ipsum dolor sit amet, consectetur adipiscing elit, sed do eiusmod tempor incididunt ut labore et dolore magna aliqua. Ut enim ad minim veniam, quis nostrud exercitation ullamco laboris nisi ut aliquip</p>
</div>
<div class="btn" style="left:627px;top:1652px;width:176px;height:46px"><span class="label">Learn More</span><span class="arrow"><svg viewBox="0 0 30 12"><path d="M0 6h27M22 1l6 5-6 5" stroke="#fff" stroke-width="2" fill="none"/></svg></span></div>

<section class="services">
  <h2 class="section-title">Our Services</h2>
  <div class="service-card" style="left:110px">
    <div class="photo" role="img" aria-label="Model house on a desk beside loan paperwork" style="background:linear-gradient(135deg,#5a524a,#b8a58c)"></div>
    <h3>Lorem ipsum dolor sit amet</h3>
    <p>Lorem ipsum dolor sit am consectetur adipiscing elit sed do eiusmod tempor incididunt ut labore et dolore magna.</p>
    <a>Read More <svg width="14" height="14" viewBox="0 0 14 14"><circle cx="7" cy="7" r="7" fill="#f7931e"/><path d="M6 4l3 3-3 3" stroke="#fff" stroke-width="1.6" fill="none"/></svg></a>
  </div>
  <div class="service-card" style="left:444px">
    <div class="photo" role="img" aria-label="Team discussing plans around a table" style="background:linear-gradient(135deg,#7b7f86,#c6c2b8)"></div>
    <h3>Lorem ipsum dolor sit amet</h3>
    <p>Lorem ipsum dolor sit am consectetur adipiscing elit sed do eiusmod tempor incididunt ut labore et dolore magna.</p>
    <a>Read More <svg width="14" height="14" viewBox="0 0 14 14"><circle cx="7" cy="7" r="7" fill="#f7931e"/><path d="M6 4l3 3-3 3" stroke="#fff" stroke-width="1.6" fill="none"/></svg></a>
  </div>
  <div class="service-card" style="left:778px">
    <div class="photo" role="img" aria-label="Couple reviewing a loan offer with an advisor" style="background:linear-gradient(135deg,#8a7a68,#d3c6b4)"></div>
    <h3>Lorem ipsum dolor sit amet</h3>
    <p>Lorem ipsum dolor sit am consectetur adipiscing elit sed do eiusmod tempor incididunt ut labore et dolore magna.</p>
    <a>Read More <svg width="14" height="14" viewBox="0 0 14 14"><circle cx="7" cy="7" r="7" fill="#f7931e"/><path d="M6 4l3 3-3 3" stroke="#fff" stroke-width="1.6" fill="none"/></svg></a>
  </div>
</section>

<h2 class="section-title" style="top:2448px">Why Choose Us</h2>
<div class="why-card" style="left:110px">
  <svg class="icon" viewBox="0 0 72 68"><path d="M22 30L40 14l18 16M26 27v14h28V27" fill="none" stroke="#333" stroke-width="2.5"/><rect x="35" y="31" width="10" height="10" fill="none" stroke="#f7931e" stroke-width="2.5"/><path d="M6 48h14l10 4h16l-2 6H28M20 58l16 6 28-12" fill="none" stroke="#333" stroke-width="2.5"/></svg>
  <h3>Lorem ipsum dolor amet</h3><p>Lorem ipsum dolor consectetur adipiscing elit, sed do eiusmod</p>
  <div class="go"><svg width="8" height="10" viewBox="0 0 8 10"><path d="M2 1l4 4-4 4" stroke="#333" stroke-width="1.5" fill="none"/></svg></div>
</div>
<div class="why-card" style="left:358px">
  <svg class="icon" viewBox="0 0 72 68"><path d="M12 30L36 8l24 22M18 25v36h36V25" fill="none" stroke="#333" stroke-width="2.5"/><circle cx="36" cy="40" r="10" fill="none" stroke="#f7931e" stroke-width="2.5"/><path d="M38 33l-5 8h6l-5 8" fill="none" stroke="#333" stroke-width="2"/></svg>
  <h3>Lorem ipsum dolor amet</h3><p>Lorem ipsum dolor consectetur adipiscing elit, sed do eiusmod</p>
  <div class="go"><svg width="8" height="10" viewBox="0 0 8 10"><path d="M2 1l4 4-4 4" stroke="#333" stroke-width="1.5" fill="none"/></svg></div>
</div>
<div class="why-card active" style="left:606px">
  <svg class="icon" viewBox="0 0 72 68"><path d="M14 4h30l8 8v40H14z" fill="none" stroke="#fff" stroke-width="2.5"/><path d="M20 20h20M20 28h16" stroke="#fff" stroke-width="2.5"/><path d="M36 46l12-11 12 11v16H36z" fill="none" stroke="#fff" stroke-width="2.5"/><circle cx="48" cy="52" r="5" fill="none" stroke="#fff" stroke-width="2"/></svg>
  <h3>Lorem ipsum dolor amet</h3><p>Lorem ipsum dolor consectetur adipiscing elit, sed do eiusmod</p>
  <div class="go"><svg width="8" height="10" viewBox="0 0 8 10"><path d="M2 1l4 4-4 4" stroke="#fff" stroke-width="1.5" fill="none"/></svg></div>
</div>
<div class="why-card" style="left:854px">
  <svg class="icon" viewBox="0 0 72 68"><rect x="24" y="4" width="32" height="40" fill="none" stroke="#333" stroke-width="2.5"/><path d="M30 14h20M30 22h20M30 30h14" stroke="#f7931e" stroke-width="2.5"/><path d="M10 44l14-12 14 12v18H10z" fill="none" stroke="#333" stroke-width="2.5"/><path d="M6 64h56" stroke="#333" stroke-width="2.5"/></svg>
  <h3>Lorem ipsum dolor amet</h3><p>Lorem ipsum dolor consectetur adipiscing elit, sed do eiusmod</p>
  <div class="go"><svg width="8" height="10" viewBox="0 0 8 10"><path d="M2 1l4 4-4 4" stroke="#333" stroke-width="1.5" fill="none"/></svg></div>
</div>

<h2 class="section-title" style="top:2826px">Our Testimonials</h2>
<div class="stars">★★★★★</div>
<p class="quote">Lorem ipsum dolor sit amet, consectetur adipiscing elit, sed do eiusmod tempor incididunt ut labore et dolore magna aliqua. Ut enim ad minim veniam, quis nostrud exercitation ullamco laboris nisi ut aliquip ex ea commodo consequat. Duis aute irure dolor in reprehenderit in voluptate velit esse cillum dolore eu fugiat nulla pariatur. Excepteur sint occaecat cupidatat non proident, sunt in culpa qui officia deserunt mollit anim id est laborumed.</p>
<svg class="abs" style="left:102px;top:2994px" width="16" height="24" viewBox="0 0 16 24"><path d="M12 2L3 12l9 10" stroke="#222" stroke-width="3" fill="none"/></svg>
<svg class="abs" style="left:1084px;top:2994px" width="16" height="24" viewBox="0 0 16 24"><path d="M4 2l9 10-9 10" stroke="#222" stroke-width="3" fill="none"/></svg>
<div class="avatar" role="img" aria-label="Client portrait" style="left:509px;top:3107px;width:52px;height:52px;background:#d9a24a"></div>
<div class="avatar" role="img" aria-label="Client portrait" style="left:639px;top:3107px;width:52px;height:52px;background:#d9a24a"></div>
<div class="avatar" role="img" aria-label="Reviewer portrait" style="left:564px;top:3094px;width:74px;height:74px;background:#3d4450;border:3px solid #fff"></div>
<div class="reviewer">Darren Okafor</div>

<section class="contact">
  <h2 class="section-title">Get In Touch</h2>
  <div class="form-field" style="left:110px;top:145px">First Name:</div>
  <div class="form-field" style="left:441px;top:145px">Last Name:</div>
  <div class="form-field" style="left:772px;top:145px">Enter Your Email:</div>
  <div class="form-field" style="left:110px;top:208px">Enter Your Number:</div>
  <div class="form-field" style="left:441px;top:208px">Address:</div>
  <div class="form-field" style="left:772px;top:208px">Any Loan Details:</div>
  <div class="message">Message:</div>
  <div class="btn" style="left:513px;top:448px;width:175px;height:46px"><span class="label">Submit Now</span><span class="arrow"><svg viewBox="0 0 30 12"><path d="M0 6h27M22 1l6 5-6 5" stroke="#fff" stroke-width="2" fill="none"/></svg></span></div>
</section>

<footer class="site-footer">
  <svg class="abs" style="left:0;top:0" width="1200" height="130" viewBox="0 0 1200 130">
    <path d="M0 0H1200V4L600 124L0 4Z" fill="#f7931e"/>
    <path d="M0 0H1200V-6L600 106L0 -6Z" fill="#fdf4ea"/>
  </svg>
  <div class="foot-col" style="left:112px"><h4>Quick Links</h4><ul><li>Home</li><li>About Us</li><li>Services</li><li>Why choose us</li><li>Contact us</li></ul></div>
  <div class="foot-col" style="left:318px"><h4>About Company</h4><ul><li>Legal Information</li><li>Terms &amp; Condition</li><li>Privacy Policy</li><li>Support</li><li>Site Map</li></ul></div>
  <div class="foot-col" style="left:547px"><h4>Newsletter</h4><p>Subscribe to our email address<br>to get the latest news</p>
    <div class="subscribe">Enter Your Email...<b><svg width="16" height="16" viewBox="0 0 16 16"><circle cx="8" cy="8" r="8" fill="#fff"/><path d="M7 4l4 4-4 4" stroke="#f7931e" stroke-width="2" fill="none"/></svg></b></div></div>
  <div class="foot-col" style="left:857px"><h4>Contact Us</h4>
    <div class="contact-row"><svg width="14" height="14" viewBox="0 0 24 24"><path d="M6.6 10.8a15 15 0 006.6 6.6l2.2-2.2a1 1 0 011-.25 11.4 11.4 0 003.6.57 1 1 0 011 1V20a1 1 0 01-1 1A17 17 0 013 4a1 1 0 011-1h3.5a1 1 0 011 1 11.4 11.4 0 00.57 3.6 1 1 0 01-.25 1z" fill="#f7931e"/></svg><div><small>Phone</small><span>+1 555 014 2290</span></div></div>
    <div class="contact-row"><svg width="14" height="12" viewBox="0 0 24 18"><rect x="0" y="0" width="24" height="18" rx="2" fill="#f7931e"/><path d="M1 2l11 8 11-8" fill="none" stroke="#1f1f24" stroke-width="2"/></svg><div><small>Email</small><span>info@talvo.example</span></div></div>
    <div class="contact-row"><svg width="14" height="16" viewBox="0 0 20 26"><path d="M10 0a9 9 0 019 9c0 7-9 17-9 17S1 16 1 9a9 9 0 019-9z" fill="#f7931e"/><circle cx="10" cy="9" r="3.5" fill="#1f1f24"/></svg><div><small>Location</small><span>123,Lorem ipsum dolor amted<br>consectetur adipiscing elited.</span></div></div>
  </div>
  <div class="to-top"><svg width="14" height="10" viewBox="0 0 14 10"><path d="M1 8l6-6 6 6" stroke="#fff" stroke-width="2" fill="none"/></svg></div>
  <div class="foot-rule"></div>
  <div class="copyright">2022 Copyright - Talvo Mortgage &nbsp;| &nbsp;All Rights Reserved</div>
</footer>

</body>
</html>
```